Two Marketing Brochures

We need two professional A4 brochures (PDF + web version) to promote our new handyman services to Facility Managers in Queensland.
Brochure 1: BRW Facilities Trade Services (see content BRW Facilities.pdf). Create new cover page and contents page then design 2 content pages (left and right) I will then paste all text myself, rather than designing 19 pages.
Brochure 2: BRW Facilities Minor Works & Maintenance – Smarter, Simpler, Cheaper
Audience: Commercial property managers, QLD Gov, councils, schools, industrial clients
Style: Clean, modern, corporate, BRW Facilities-branded
Content: Text is finalised and ready to go
Deliverables: A4 PDF (print-ready) + web version (compressed)
Optional: Integration of TaskLoop7 elements (e.g. “Book Now” QR or icon)

```html
<!DOCTYPE html>
<html lang="en">
<head>
<meta charset="utf-8">
<title>BRW Facilities – Trade Services Brochure</title>
<link href="https://fonts.googleapis.com/css2?family=Montserrat:wght@400;500;600;700;800&display=swap" rel="stylesheet">
<style>
  :root {
    --navy: #1c3d5a;
    --navy-dark: #173450;
    --band: #d2dbe1;
    --paper: #ffffff;
    --backdrop: #ebe8e3;
    --badge-red: #e0323c;
    --badge-green: #2f9a45;
    --badge-yellow: #f2b81c;
  }
  * { box-sizing: border-box; margin: 0; padding: 0; }
  html, body { width: 1200px; height: 960px; overflow: hidden; }
  body {
    background: var(--backdrop);
    font-family: "Montserrat", sans-serif;
    color: var(--navy);
    position: relative;
  }
  .page {
    position: absolute;
    top: 67px;
    height: 765px;
    background: var(--paper);
    box-shadow: 0 3px 10px rgba(0,0,0,.25);
    overflow: hidden;
  }
  .page--cover { left: 53px; width: 539px; }
  .page--policy { left: 614px; width: 542px; }

  /* wordmark */
  .brand { position: absolute; display: flex; align-items: center; color: var(--navy); }
  .brand__name { font-weight: 800; letter-spacing: .5px; }
  .brand__divider { width: 1px; background: var(--navy); margin: 0 7px; align-self: stretch; }
  .brand__sub { font-weight: 400; letter-spacing: 1px; }
  .cover__brand { left: 41px; top: 56px; height: 40px; }
  .cover__brand .brand__name { font-size: 36px; }
  .cover__brand .brand__sub { font-size: 20px; }
  .policy__brand { left: 375px; top: 36px; height: 28px; }
  .policy__brand .brand__name { font-size: 22px; }
  .policy__brand .brand__sub { font-size: 11px; }

  .badges { position: absolute; left: 336px; top: 54px; display: flex; gap: 10px; }
  .badge { width: 46px; height: 46px; border-radius: 50%; border: 2px solid #f0d6d6; background: #fff; display: flex; align-items: center; justify-content: center; }
  .badge span { width: 26px; height: 26px; border-radius: 50%; }
  .badge--quality span { background: var(--badge-red); }
  .badge--environment span { background: var(--badge-green); }
  .badge--safety span { background: var(--badge-yellow); }

  .cover__title { position: absolute; left: 46px; top: 137px; font-size: 29.5px; font-weight: 800; letter-spacing: .2px; }
  .cover__subtitle { position: absolute; left: 45px; top: 175px; font-size: 14.6px; font-weight: 500; letter-spacing: .2px; }

  .cover__photos { position: absolute; left: 0; top: 237px; width: 539px; height: 373px; }
  .photo { position: absolute; }
  .photo--pipes { left: 0; top: 0; width: 261px; height: 176px; background: linear-gradient(160deg, #8c8c86, #b55a3a 55%, #3e4f7a); }
  .photo--switchboard { left: 275px; top: 0; width: 264px; height: 176px; background: linear-gradient(200deg, #d6d6d2, #e0c24a 45%, #5a5f66); }
  .photo--pumps { left: 0; top: 198px; width: 261px; height: 175px; background: linear-gradient(180deg, #9a9a94, #7a3a2c 55%, #3d5f7e); }
  .photo--aircon { left: 275px; top: 198px; width: 264px; height: 175px; background: linear-gradient(120deg, #c9d1d6, #b48a7e 55%, #6f6c66); }

  .cover__tagline { position: absolute; left: 52px; top: 640px; font-size: 17.5px; font-weight: 800; line-height: 21px; }
  .cover__intro { position: absolute; left: 262px; top: 643px; width: 249px; font-size: 10.8px; font-weight: 700; line-height: 13.2px; text-align: justify; }

  /* policy page */
  .policy__heading { position: absolute; left: 45px; top: 37px; font-size: 16px; font-weight: 800; letter-spacing: .3px; }
  .policy__band { position: absolute; left: 0; top: 110px; width: 52px; height: 610px; background: var(--band); }
  .policy__label {
    position: absolute; left: 45px; height: 22px; padding: 0 8px;
    background: var(--navy-dark); color: #fff;
    font-size: 10px; font-weight: 700; line-height: 22px; letter-spacing: .3px; white-space: nowrap;
  }
  .policy__connector { position: absolute; height: 1px; background: var(--navy); }
  .policy__bracket { position: absolute; left: 210px; width: 20px; border: 1px solid var(--navy); border-right: none; }
  .policy__list { position: absolute; left: 227px; width: 282px; list-style: none; font-size: 9px; line-height: 11.1px; color: #1a1a1a; }
</style>
</head>
<body>

<section class="page page--cover">
  <div class="brand cover__brand">
    <span class="brand__name">BRW</span><span class="brand__divider"></span><span class="brand__sub">FACILITIES</span>
  </div>
  <div class="badges" aria-label="Certification badges">
    <div class="badge badge--quality"><span></span></div>
    <div class="badge badge--environment"><span></span></div>
    <div class="badge badge--safety"><span></span></div>
  </div>
  <h1 class="cover__title">Facilities Trade Services</h1>
  <p class="cover__subtitle">APPLIANCES, PLUMBING, ELECTRICAL, HEATING &amp; COOLING</p>

  <div class="cover__photos">
    <div class="photo photo--pipes" role="img" aria-label="Photo of copper and coloured service pipes in a plant room"></div>
    <div class="photo photo--switchboard" role="img" aria-label="Photo of hands working on an electrical switchboard"></div>
    <div class="photo photo--pumps" role="img" aria-label="Photo of red pumps and valves in a plant room"></div>
    <div class="photo photo--aircon" role="img" aria-label="Photo of an outdoor air-conditioning unit beside a building"></div>
  </div>

  <h2 class="cover__tagline">LEGENDARY<br>SERVICE,<br>DELIVERED DAILY</h2>
  <p class="cover__intro">BRW is Plumbing, Electrical, Heating, and Cooling on demand. With easy bookings, solid van tracking door-to-door, and goodlooking reports, we’re guaranteed to get the job done.</p>
</section>

<section class="page page--policy">
  <h2 class="policy__heading">SERVICE POLICY</h2>
  <div class="brand policy__brand">
    <span class="brand__name">BRW</span><span class="brand__divider"></span><span class="brand__sub">FACILITIES</span>
  </div>
  <div class="policy__band"></div>

  <div class="policy__label" style="top:163px">NORMAL HOURS SERVICE</div>
  <div class="policy__connector" style="left:191px;top:174px;width:19px"></div>
  <div class="policy__bracket" style="top:124px;height:92px"></div>
  <ul class="policy__list" style="top:126px">
    <li>- Service call includes first 15 minutes of labour.</li>
    <li>- Labour is then charged per 15-minute block thereafter.</li>
    <li>- Complete only requested or approved works.</li>
    <li>- All required material, sundries, and compliance will be charged as additional to service and labour.</li>
    <li>- Photos: before and after.</li>
    <li>- Removal and disposal of all rubbish related to works.</li>
    <li>- Area cleaned upon completion of work.</li>
  </ul>

  <div class="policy__label" style="top:237px">Works Do Not Include</div>
  <div class="policy__connector" style="left:191px;top:248px;width:19px"></div>
  <div class="policy__bracket" style="top:225px;height:36px"></div>
  <ul class="policy__list" style="top:227px">
    <li>- Moving of any heavy/bulky furniture to access faults.</li>
    <li>- Any major remedial works/repairs or replacements without prior written direction/budget approval.</li>
  </ul>

  <div class="policy__label" style="top:321px">Important Notes</div>
  <div class="policy__connector" style="left:147px;top:332px;width:63px"></div>
  <div class="policy__bracket" style="top:269px;height:114px"></div>
  <ul class="policy__list" style="top:271px">
    <li>- If further works are required (beyond the initial scope or budget) — unless requested — we will not invoice the original work order, instead, we will hold the original job open for 5 days for the property manager to seek authorisation for further works. This way, the property manager will avoid having multiple work orders and invoices for a single job.</li>
    <li>- After 5 days of no action or further approval, we will invoice the first attendance and wait on a new work order for further works.</li>
  </ul>

  <div class="policy__label" style="top:443px">AFTER HOURS SERVICE</div>
  <div class="policy__connector" style="left:184px;top:454px;width:26px"></div>
  <div class="policy__bracket" style="top:393px;height:113px"></div>
  <ul class="policy__list" style="top:394px">
    <li>- Service does not include any labour.</li>
    <li>- Minimum charge of 1-hour labour.</li>
    <li>- After-hours loading (includes total trip travel up to 30km).</li>
    <li>- Labour is charged per 15-minute block after the first hour.</li>
    <li>- Qualify over the phone if the job is ‘urgent’ per the Residential Tenancies Act (list of urgent repairs).</li>
    <li>- Complete minimum works to make the site safe and habitable.</li>
    <li>- Complete minor repairs/replacements to avoid re attendance.</li>
  </ul>

  <div class="policy__label" style="top:533px">Works Do Not Include</div>
  <div class="policy__connector" style="left:184px;top:544px;width:26px"></div>
  <div class="policy__bracket" style="top:523px;height:44px"></div>
  <ul class="policy__list" style="top:524px">
    <li>- Moving of any heavy/bulky furniture to access faults (area must be cleared by renters when reasonable to do so).</li>
    <li>- Any major remedial works/repairs or replacements.</li>
    <li>- Any removal of trade waste from site.</li>
  </ul>

  <div class="policy__label" style="top:634px">Important Notes</div>
  <div class="policy__connector" style="left:147px;top:645px;width:63px"></div>
  <div class="policy__bracket" style="top:587px;height:139px"></div>
  <ul class="policy__list" style="top:590px">
    <li>- Works where excessive noise will be generated (rotary drilling, sewer cabling, etc.), the attending technician will at their discretion decide if this is suitable given the time of day and impact of noise pollution to neighbours (e.g., cabling a sewer after 5 pm).</li>
    <li>- Works will only be attempted where the work area is deemed safe.</li>
    <li>- Where temporary services (e.g., hot water units) are installed, all trade waste related to the faulty/decommissioned unit will remain on-site and only removed once permanent replacement is approved in writing (temporary services only installed where suitable).</li>
  </ul>
</section>

</body>
</html>
```